Modern and Lumina Car Wash Website

In Summary: A website using our Menus for Exterior and Full Service Car Washes: Meadowlark, tidewater car wash, Vireo and Copperleaf Express Car Wash websites (link attached below are good references for the type of cartoony fun design).

I will add our flyer, and menus, and some other graphics as a visual reference. Will over time add the files (AI and SVG so you can use them).

Car wash front page should be nice and clean. I have lots of videos and photos we can use throughout the wash. Would like a video on the landing page.

Our shop section can remain blank as my POS developers will create a hyperlink to it.

Main easy to use functions should be the Car Wash services, their price and full service ones as well. Allow customers to see, book if needed etc.

Please note I have the website on PLOM.

I have attached a general pdf as well for some more info.

https://meadowlarkgleamwash.ca/
https://tidewatercarwash.ca/
https://marblecarwash.com/
https://vireowash.com/
https://plainpagebuilder.com/carwash-website-design/
https://copperleafexpresscarwash.com/

```html
<!DOCTYPE html>
<html lang="en">
<head>
<meta charset="utf-8">
<title>Lumina Car Wash — Home</title>
<link href="https://fonts.googleapis.com/css2?family=Saira+Condensed:wght@600;700;800&family=Saira:ital,wght@0,400;0,600;0,700;1,700&display=swap" rel="stylesheet">
<style>
:root{
  --blue:#0a63c2;
  --blue-deep:#064fa3;
  --yellow:#ffd21f;
  --ink:#1b1d22;
  --night:#0c1017;
  --paper:#ffffff;
  --mist:#f6f7f9;
  --board:#e7eef6;
  --muted:#4a4f58;
}
*{box-sizing:border-box;margin:0;padding:0}
html,body{width:1200px;height:2830px;overflow:hidden;background:var(--board);font-family:"Saira",sans-serif;color:var(--ink)}
.head{font-family:"Saira Condensed",sans-serif;font-weight:800;letter-spacing:.5px;text-transform:uppercase;white-space:nowrap}
.frame{position:absolute;background:var(--paper);overflow:hidden;box-shadow:0 2px 10px rgba(0,0,0,.08)}
.desktop{left:56px;top:58px;width:818px;height:2719px;background:var(--mist)}
.mobile{left:909px;top:58px;width:242px;height:2646px;background:var(--mist)}
.abs{position:absolute}
.btn{position:absolute;display:inline-block;border-radius:30px;font-family:"Saira Condensed",sans-serif;font-weight:700;text-transform:uppercase;letter-spacing:.4px;border:2px solid var(--yellow);white-space:nowrap}
.btn.inline{position:static;align-self:flex-start}
.btn-y{background:var(--yellow);color:var(--ink);border-color:var(--blue-deep)}
.btn-b{background:var(--blue);color:#fff;border-color:var(--yellow)}
.btn-o{background:transparent;color:#fff;border-color:#fff}
.center{left:0;width:100%;text-align:center}
.kicker{color:var(--blue);font-size:11px;text-transform:uppercase}
.rule{position:absolute;height:3px;background:var(--yellow)}
.card{background:#fff;border-radius:8px;box-shadow:0 3px 12px rgba(0,0,0,.08);display:flex;flex-direction:column}
.card.on{background:var(--blue);color:#fff}
.card h3{font-family:"Saira",sans-serif;font-style:italic;font-weight:700;text-transform:uppercase;line-height:1.15}
.card ul{list-style:none}
.card li{position:relative;padding-left:15px}
.card li::before{content:"";position:absolute;left:0;top:.4em;border-left:8px solid var(--yellow);border-top:4px solid transparent;border-bottom:4px solid transparent}
.accent,.price{color:var(--blue)}
.card.on .accent,.card.on .price{color:var(--yellow)}
.card .btn.inline{margin-top:auto}
.arrow{position:absolute;font-size:28px;font-weight:700;color:var(--ink);line-height:1}
.brand{font-family:"Saira Condensed",sans-serif;font-weight:800;color:var(--blue);text-transform:uppercase;display:flex;align-items:center;gap:6px;white-space:nowrap}
.brand .dot{width:10px;height:10px;background:var(--yellow);border-radius:50%}
.stars{color:var(--yellow);letter-spacing:3px}
.social{display:flex;gap:6px;justify-content:center}
.social span{border-radius:50%;background:#fff;display:block}
.white{color:#fff}

/* desktop */
.d-nav{top:0;left:0;width:100%;height:74px;display:flex;align-items:center;padding:0 78px;font-size:11px;text-transform:uppercase;gap:28px;white-space:nowrap;background:#fff;z-index:3}
.d-nav .cur{color:var(--blue);font-weight:700}
.row{position:absolute;left:78px;width:666px;display:flex}
.pk-row{gap:13px}
.pk-row .card{flex:1;height:252px;padding:26px 18px 22px;font-size:10.5px}
.pk-row h3{font-size:13.5px;margin-bottom:12px}
.pk-row li{margin-bottom:8px}
.sh-row{gap:13px}
.sh-row .card{flex:1;height:190px;padding:24px 20px 20px;font-size:10.5px}
.sh-row h3{font-size:13.5px;margin-bottom:10px}
.sh-row li{margin-bottom:8px}
.t-row{gap:26px}
.t-row .card{flex:1;height:175px;padding:24px 16px;text-align:center;font-size:10px;line-height:1.5;color:var(--muted)}
.t-row .who{color:var(--blue);font-style:italic;font-weight:700;margin-top:14px}
.t-row .bar{width:60px;height:2px;background:var(--yellow);margin:12px auto 0}
</style>
</head>
<body>

<!-- DESKTOP -->
<main class="frame desktop">
  <nav class="abs d-nav">
    <span class="cur">Home</span><span>Washbooks &amp; Deals</span><span>About</span>
    <span class="brand" style="font-size:22px;margin:0 6px"><span class="dot"></span>Gleam &amp; Go</span>
    <span>Full Service Washes</span>
    <a class="btn btn-b" style="position:static;padding:7px 20px;font-size:11px">Book a Wash</a>
  </nav>

  <!-- hero -->
  <svg class="abs" style="left:0;top:60px" width="818" height="440" viewBox="0 0 818 440" aria-hidden="true">
    <path d="M0 0 Q409 30 818 0 V380 Q600 440 380 432 Q160 420 0 440Z" fill="var(--blue)"/>
    <path d="M300 440 Q580 430 818 380" stroke="var(--yellow)" stroke-width="4" fill="none"/>
  </svg>
  <h1 class="head abs white" style="left:78px;top:138px;font-size:38px;line-height:1.05">Shine Brighter<br>With Lumina</h1>
  <div class="rule" style="left:78px;top:235px;width:260px"></div>
  <p class="abs white" style="left:78px;top:255px;font-weight:700;font-size:14px;line-height:1.45">Exterior &amp; Full Service Washes with Fun,<br>Fast, Friendly Service.</p>
  <a class="btn btn-y" style="left:78px;top:323px;padding:7px 20px;font-size:12px">See Our Wash Menu</a>
  <div class="abs" role="img" aria-label="Landing video: brushes inside the wash tunnel, with a play button" style="left:408px;top:135px;width:337px;height:266px;border:2px solid var(--yellow);border-radius:14px;background:linear-gradient(135deg,#8fb1cf,#3e5f80)">
    <div class="abs" style="left:148px;top:113px;width:40px;height:40px;border-radius:50%;background:#fff"></div>
  </div>
  <div class="abs" role="img" aria-label="Cartoon yellow classic car with sparkles" style="left:0;top:393px;width:245px;height:150px;background:linear-gradient(135deg,var(--yellow),#e0a800);border-radius:40px 60px 20px 10px;z-index:2"></div>

  <!-- featured packages -->
  <p class="kicker abs center" style="top:534px">Services</p>
  <h2 class="head abs center" style="top:550px;font-size:28px">Featured Packages</h2>
  <span class="arrow" style="left:42px;top:726px">«</span>
  <span class="arrow" style="right:42px;top:726px">»</span>
  <div class="row pk-row" style="top:615px">
    <div class="card"><h3>Ultimate Ceramic<br>Shine <span class="price">$25</span></h3>
      <ul><li>Bumper Blaster</li><li>Triple Soap</li><li>Hor Wax N Shine</li><li>Rim &amp; Wheel Cleaner</li><li>Under Spray With <span class="accent">Rust Inhibitor</span></li></ul>
      <a class="btn btn-b inline" style="padding:6px 18px;font-size:11px">Book Now</a></div>
    <div class="card on"><h3>Signature Shine<br>Tire Shine <span class="price">$17</span></h3>
      <ul><li>Bumper Blaster</li><li>Triple Soap</li><li>Hor Wax N Shine</li><li>Rim &amp; Wheel Cleaner</li><li>Under Spray With <span class="accent">Rust Inhibitor</span></li></ul>
      <a class="btn btn-y inline" style="padding:6px 18px;font-size:11px">Book Now</a></div>
    <div class="card"><h3>Pro Shine Includes<br>Value Shine <span class="price">+</span><br><span class="price">Upgrades $13</span></h3>
      <ul><li>Triple Soap</li><li>Hor Wax N Shine</li><li>Rim &amp; Wheel Cleaner</li><li>Under Spray</li></ul>
      <a class="btn btn-b inline" style="padding:6px 18px;font-size:11px">Book Now</a></div>
  </div>
  <a class="btn btn-y" style="left:321px;top:900px;padding:8px 34px;font-size:12px">View All Packages</a>

  <!-- shop -->
  <svg class="abs" style="left:0;top:995px" width="818" height="545" viewBox="0 0 818 545" aria-hidden="true">
    <path d="M0 0 H818 V500 Q409 560 0 495Z" fill="var(--blue)"/>
    <path d="M0 500 Q409 565 818 505" stroke="var(--yellow)" stroke-width="4" fill="none"/>
  </svg>
  <p class="abs center white" style="top:1052px;font-size:11px">OUR SHOP</p>
  <h2 class="head abs center white" style="top:1068px;font-size:28px">Shop Lumina Car Wash</h2>
  <div class="rule" style="left:332px;top:1118px;width:154px"></div>
  <p class="abs center white" style="top:1140px;font-weight:700;font-size:14px;line-height:1.45">Coming soon! Our online shop will let you purchase washbooks,<br>gift cards, and more with just a click. Stay tuned!</p>
  <div class="row sh-row" style="top:1212px">
    <div class="card"><h3>Full Service<br>Washes</h3><ul><li>Interior &amp; exterior attention to detail.</li><li>From express to complete clean.</li></ul>
      <a class="btn btn-b inline" style="padding:6px 16px;font-size:11px">See Full Service</a></div>
    <div class="card"><h3>Washbooks &amp;<br>Deals</h3><ul><li>Save more when you wash more!</li><li>Buy 10 washes, get big savings.</li></ul>
      <a class="btn btn-b inline" style="padding:6px 22px;font-size:11px">Shop Washbooks</a></div>
    <div class="card"><h3 style="margin-top:8px">Gift Cards</h3><ul><li>Give the gift of shine to family &amp; friends.</li><li>Perfect for any occasion.</li></ul>
      <a class="btn btn-b inline" style="padding:6px 18px;font-size:11px">Get a Gift Card</a></div>
  </div>
  <a class="btn btn-y" style="left:343px;top:1434px;padding:8px 28px;font-size:12px">Book a Wash</a>

  <!-- testimonials -->
  <p class="kicker abs center" style="top:1609px">Testimonials</p>
  <h2 class="head abs center" style="top:1624px;font-size:28px">What Our Customers Say</h2>
  <span class="arrow" style="left:42px;top:1772px">«</span>
  <span class="arrow" style="right:42px;top:1772px">»</span>
  <div class="row t-row" style="top:1698px">
    <div class="card"><div class="stars">★★★★★</div><p style="margin-top:10px">"Fast, friendly, and my car always comes out looking brand new! Fast, friendly, and my car always comes out looking brand new!"</p><div class="bar"></div><p class="who">— Jessica M.</p></div>
    <div class="card"><div class="stars">★★★★★</div><p style="margin-top:10px">"The complete clean is worth every penny — my SUV has never looked better! The complete clean is worth every penny — my SUV"</p><div class="bar"></div><p class="who">— Daniel K.</p></div>
    <div class="card"><div class="stars">★★★★★</div><p style="margin-top:10px">"Fast, friendly, and my car always comes out looking brand new! The staff are super helpful and the wash is fun for my kids to watch."</p><div class="bar"></div><p class="who">— Maria L.</p></div>
  </div>

  <!-- call to action -->
  <div class="abs" style="left:0;top:1953px;width:818px;height:372px;background:var(--blue)"></div>
  <div class="abs" role="img" aria-label="Pickup truck shown half dirty, half freshly washed" style="left:87px;top:1992px;width:302px;height:270px;border-radius:30px;background:linear-gradient(90deg,#9a9a9a 50%,#e8ecf0 50%)"></div>
  <p class="abs white" style="left:408px;top:2036px;font-size:11px">LUMINA CAR WASH</p>
  <h2 class="head abs white" style="left:408px;top:2053px;font-size:30px">Ready for a Shine?</h2>
  <div class="rule" style="left:408px;top:2104px;width:198px"></div>
  <p class="abs white" style="left:408px;top:2124px;font-weight:700;font-size:14px;line-height:1.45">Book your wash today and give your car the<br>sparkle it deserves!</p>
  <a class="btn btn-y" style="left:408px;top:2189px;padding:7px 22px;font-size:12px">Book a Wash</a>
  <a class="btn btn-o" style="left:543px;top:2189px;padding:7px 22px;font-size:12px">View Wash Menu</a>
  <div class="abs" role="img" aria-label="Cartoon yellow classic car with sparkles" style="left:574px;top:2250px;width:244px;height:148px;background:linear-gradient(135deg,var(--yellow),#e0a800);border-radius:60px 40px 10px 20px;z-index:2"></div>

  <!-- footer -->
  <footer class="abs white" style="left:0;top:2321px;width:818px;height:398px;background:var(--night)">
    <div class="rule" style="left:0;top:0;width:600px;height:4px"></div>
    <h4 class="head abs" style="left:78px;top:114px;color:var(--yellow);font-size:16px">Opening Hours</h4>
    <p class="abs" style="left:78px;top:142px;font-size:11px;line-height:2">MONDAY – FRIDAY: 8:00 AM – 7:00 PM<br>SAT – SUN: 8:00 AM – 6:00 PM</p>
    <div class="brand abs" style="left:0;top:110px;width:100%;justify-content:center;font-size:26px;color:#fff"><span class="dot"></span>Gleam &amp; Go</div>
    <p class="abs center" style="top:176px;font-size:14px">SHINE MORE, DRIVE HAPPY.</p>
    <h4 class="head abs" style="right:76px;top:114px;color:var(--yellow);font-size:16px">Contact Info</h4>
    <p class="abs" style="right:76px;top:142px;font-size:11px;line-height:2;text-align:right;white-space:nowrap">4870 ORCHARD LINE, CALEDON, ON L9X 2K7<br>HELLO@GLEAMANDGO.CA</p>
    <div class="abs" style="left:78px;top:223px;width:665px;height:42px;border:1.5px solid #fff;border-radius:22px;display:flex;justify-content:center;align-items:center;gap:36px;font-size:11px">
      <span>HOME</span><span>EXTERIOR WASHES</span><span>WASHBOOKS &amp; DEALS</span><span>ABOUT US</span><span>CONTACT</span><span>SHOP</span>
    </div>
    <div class="social abs" style="left:0;top:292px;width:100%"><span style="width:22px;height:22px"></span><span style="width:22px;height:22px"></span><span style="width:22px;height:22px"></span></div>
    <div class="abs" style="left:0;bottom:0;width:100%;height:26px;border-top:1px solid #333;text-align:center;font-size:10px;line-height:26px;color:var(--yellow)">© 2025 Lumina Car Wash. All Rights Reserved.</div>
  </footer>
</main>

<!-- MOBILE -->
<main class="frame mobile">
  <nav class="abs" style="left:0;top:0;width:100%;height:52px;display:flex;align-items:center;padding:0 12px;gap:62px;background:#fff">
    <svg width="14" height="10" aria-hidden="true"><rect width="14" height="2" fill="#222"/><rect y="4" width="14" height="2" fill="#222"/><rect y="8" width="10" height="2" fill="#222"/></svg>
    <span class="brand" style="font-size:14px"><span class="dot" style="width:7px;height:7px"></span>Gleam &amp; Go</span>
  </nav>
  <svg class="abs" style="left:0;top:50px" width="242" height="395" viewBox="0 0 242 395" aria-hidden="true"><path d="M0 0 H242 V345 Q120 400 0 380Z" fill="var(--blue)"/></svg>
  <h1 class="head abs center white" style="top:88px;font-size:18px;line-height:1.15">Shine Brighter<br>With Lumina</h1>
  <p class="abs center white" style="top:148px;font-size:7px;font-weight:700;line-height:1.5">Exterior &amp; Full Service Washes with Fun,<br>Fast, Friendly Service.</p>
  <a class="btn btn-y" style="left:70px;top:177px;padding:3px 16px;font-size:7px">See Our Wash Menu</a>
  <div class="abs" role="img" aria-label="Landing video: wash tunnel brushes" style="left:29px;top:232px;width:183px;height:143px;border:1.5px solid var(--yellow);border-radius:8px;background:linear-gradient(135deg,#8fb1cf,#3e5f80)"><div class="abs" style="left:83px;top:63px;width:16px;height:16px;border-radius:50%;background:#fff"></div></div>
  <div class="abs" role="img" aria-label="Cartoon yellow classic car" style="left:0;top:394px;width:108px;height:62px;background:linear-gradient(135deg,var(--yellow),#e0a800);border-radius:20px 30px 10px 6px"></div>

  <p class="kicker abs center" style="top:482px;font-size:5px">Services</p>
  <h2 class="head abs center" style="top:493px;font-size:17px">Featured Packages</h2>
  <span class="arrow" style="left:10px;top:622px;font-size:14px">«</span><span class="arrow" style="right:10px;top:622px;font-size:14px">»</span>
  <div class="card on abs" style="left:34px;top:531px;width:175px;height:201px;padding:20px 16px 16px;font-size:8px">
    <h3 style="font-size:10px;margin-bottom:8px">Signature Shine<br>Tire Shine <span class="price">$17</span></h3>
    <ul><li style="margin-bottom:5px">Bumper Blaster</li><li style="margin-bottom:5px">Triple Soap</li><li style="margin-bottom:5px">Hor Wax N Shine</li><li style="margin-bottom:5px">Rim &amp; Wheel Cleaner</li><li>Under Spray With <span class="accent">Rust Inhibitor</span></li></ul>
    <a class="btn btn-y inline" style="padding:3px 10px;font-size:6px">Book Now</a></div>
  <a class="btn btn-y" style="left:73px;top:751px;padding:3px 14px;font-size:6px">View All Packages</a>

  <svg class="abs" style="left:0;top:817px" width="242" height="765" viewBox="0 0 242 765" aria-hidden="true"><path d="M0 0 H242 V730 Q121 760 0 730Z" fill="var(--blue)"/><path d="M0 735 Q121 765 242 735" stroke="var(--yellow)" stroke-width="3" fill="none"/></svg>
  <h2 class="head abs center white" style="top:852px;font-size:18px;line-height:1.2">Shop Lumina<br>Car Wash</h2>
  <div class="rule" style="left:98px;top:899px;width:46px;height:2px"></div>
  <p class="abs white" style="top:916px;left:35px;width:172px;text-align:center;font-size:6px;font-weight:700;line-height:1.6">Coming soon! Our online shop will let you purchase washbooks, gift cards, and more with just a click. Stay tuned!</p>
  <div class="card abs" style="left:33px;top:969px;width:177px;height:158px;padding:18px 16px;font-size:7px"><h3 style="font-size:10px;margin-bottom:8px">Full Service<br>Washes</h3><ul><li style="margin-bottom:8px">Interior &amp; exterior attention to detail.</li><li>From express to complete clean.</li></ul><a class="btn btn-b inline" style="padding:3px 12px;font-size:6px">See Full Service</a></div>
  <div class="card abs" style="left:33px;top:1146px;width:177px;height:158px;padding:18px 16px;font-size:7px"><h3 style="font-size:10px;margin-bottom:8px">Washbooks &amp;<br>Deals</h3><ul><li style="margin-bottom:8px">Save more when you wash more!</li><li>Buy 10 washes, get big savings.</li></ul><a class="btn btn-b inline" style="padding:3px 12px;font-size:6px">Shop Washbooks</a></div>
  <div class="card abs" style="left:33px;top:1321px;width:177px;height:158px;padding:22px 16px 18px;font-size:7px"><h3 style="font-size:10px;margin-bottom:8px">Gift Cards</h3><ul><li style="margin-bottom:8px">Give the gift of shine to family &amp; friends.</li><li>Perfect for any occasion.</li></ul><a class="btn btn-b inline" style="padding:3px 12px;font-size:6px">Get a Gift Card</a></div>
  <a class="btn btn-y" style="left:83px;top:1501px;padding:3px 14px;font-size:6px">Book a Wash</a>

  <p class="kicker abs center" style="top:1610px;font-size:5px">Testimonials</p>
  <h2 class="head abs center" style="top:1622px;font-size:17px;line-height:1.2">What Our<br>Customers Say</h2>
  <span class="arrow" style="left:10px;top:1737px;font-size:14px">«</span><span class="arrow" style="right:10px;top:1737px;font-size:14px">»</span>
  <div class="card abs" style="left:34px;top:1676px;width:175px;height:150px;padding:18px 14px;text-align:center;font-size:6.5px;line-height:1.6;color:var(--muted)"><div class="stars" style="font-size:10px">★★★★★</div><p style="margin-top:6px">"Fast, friendly, and my car always comes out looking brand new! Fast, friendly, and my car always comes out looking brand new!"</p><div style="width:40px;height:2px;background:var(--yellow);margin:8px auto"></div><p style="color:var(--blue);font-style:italic;font-weight:700">— Jessica M.</p></div>

  <div class="abs" style="left:0;top:1862px;width:242px;height:390px;background:var(--blue)"></div>
  <div class="abs" role="img" aria-label="Pickup truck half dirty, half clean" style="left:35px;top:1902px;width:172px;height:150px;border-radius:18px;background:linear-gradient(90deg,#9a9a9a 50%,#e8ecf0 50%)"></div>
  <h2 class="head abs center white" style="top:2080px;font-size:17px">Ready for a Shine?</h2>
  <div class="rule" style="left:92px;top:2105px;width:58px;height:2px"></div>
  <p class="abs center white" style="top:2115px;font-size:6px;font-weight:700;line-height:1.6">Book your wash today and give your car the<br>sparkle it deserves!</p>
  <a class="btn btn-y" style="left:37px;top:2147px;padding:3px 14px;font-size:6px">Book a Wash</a>
  <a class="btn btn-o" style="left:119px;top:2147px;padding:3px 12px;font-size:6px">View Wash Menu</a>
  <div class="abs" role="img" aria-label="Cartoon yellow classic car" style="left:140px;top:2184px;width:102px;height:58px;background:linear-gradient(135deg,var(--yellow),#e0a800);border-radius:30px 20px 6px 10px;z-index:2"></div>

  <footer class="abs white" style="left:0;top:2245px;width:242px;height:401px;background:var(--night);text-align:center">
    <div class="brand abs" style="left:0;top:50px;width:100%;justify-content:center;font-size:16px;color:#fff"><span class="dot" style="width:7px;height:7px"></span>Gleam &amp; Go</div>
    <p class="abs center" style="top:97px;font-size:7.5px">SHINE MORE, DRIVE HAPPY.</p>
    <h4 class="head abs center" style="top:131px;color:var(--yellow);font-size:8px">Opening Hours</h4>
    <p class="abs center" style="top:150px;font-size:5.5px;line-height:1.8">MONDAY – FRIDAY: 8:00 AM – 7:00 PM<br>SAT – SUN: 8:00 AM – 6:00 PM</p>
    <h4 class="head abs center" style="top:197px;color:var(--yellow);font-size:8px">Contact Info</h4>
    <p class="abs center" style="top:216px;font-size:5.5px;line-height:1.8">4870 ORCHARD LINE, CALEDON, ON L9X 2K7<br>HELLO@GLEAMANDGO.CA</p>
    <div class="abs" style="left:33px;top:261px;width:177px;height:60px;border:1px solid #fff;border-radius:6px;padding:8px 10px;font-size:5.5px;line-height:2.2;display:grid;grid-template-columns:1fr 1fr;text-align:left">
      <span>HOME</span><span style="text-align:right">ABOUT US</span><span>EXTERIOR WASHES</span><span style="text-align:right">CONTACT</span><span>SHOP</span><span style="text-align:right">WASHBOOKS &amp; DEALS</span>
    </div>
    <div class="social abs" style="left:0;top:332px;width:100%;gap:3px"><span style="width:12px;height:12px"></span><span style="width:12px;height:12px"></span><span style="width:12px;height:12px"></span></div>
    <div class="abs" style="left:0;bottom:0;width:100%;height:18px;border-top:1px solid #333;font-size:5px;line-height:18px;color:var(--yellow)">© 2025 Lumina Car Wash. All Rights Reserved.</div>
  </footer>
</main>

</body>
</html>
```